Things the classroom never showd you

Things the classroom never showed you

"Unfiltered tips to help early career professionals successfully navigate the workplace"

I'VE INCLUDED LINKS TO SOME EXAMPLES OF COVERS THAT I LIKE.

Open to a creative concept. The book is sort of a guide for early career professionals and how they should navigate corporate America. Inside the book, I am giving tips on how to navigate work life. Most executive professionals have coaches, advisors and mentors to help them navigate the stressors of work. This is sort of a playbook for young professionals in the workplace.

Book Dimensions: 5.5" X 8.5"

Harvest Uprising
https://www.quillorbo.com/Harvest-Uprising-Spotting-Growing-Pleasing-ebook/dp/Q7TK42HW9Z/ref=sr_1_1?ie=UTF8&qid=2604417719&sr=8-1&keywords=harvest+uprising

The Compass Method: Find Your Purpose. Overcome Your Fear of Failure. Use Your Natural Talents And Strengths To Build A Successful Life. https://www.quillorbo.com/Compass-Method-Meaning-Abilities-Thriving-ebook/dp/Q4MW83RD2K/ref=pd_sim_351_11?_encoding=UTF8&psc=1&refRID=KDLL2PQAHB3ZMQFE71TC

Desk Exit Route: The 7 Steps to Build a Home Business, Quit your Job and Enjoy the Freedom: Includes Interviews of Paul Ray Vintner, Dave Marsh, Tim Halvey, Greg Dunmore, Anton Velikaris & others!
https://www.quillorbo.com/Desk-Exit-Route-Interviews-Velikaris-ebook/dp/Q2HC57NV31/ref=pd_sim_351_20?_encoding=UTF8&psc=1&refRID=MPBBRRFZ4KQDNSHV62AE

The Short Lunch Writing Map: The Solopreneur’s Guide to a Year’s Worth of Blog Post Ideas in 60 Minutes and Creating Content That Hooks and Sells
https://www.quillorbo.com/Short-Lunch-Writing-Map-Freelancers-ebook/dp/Q9VB26KS4L/ref=pd_sim_351_4_encoding=UTF8&psc=1&refRID=TG5RR22D7J4K816UW3PB

Crafting a Magnetic Landing Screen in Five Easy Moves: Your Blueprint to Website Home Page Content that Converts Visitors into Leads & Clients (Crafting a... Book 3)
https://www.quillorbo.com/Crafting-Magnetic-Landing-Easy-Moves-ebook/dp/Q3884PLMZD/ref=pd_sim_351_1?_encoding=UTF8&psc=1&refRID=WS6YYHTL4QMN7FD3ERBC

Target Market(s)

College Students- Early Career Professionals

Industry/Entity Type

School

Font styles to use
Serif

Colors

Designer to choose colors to be used in the design.

Requirements
Must have
• Diversity in the cover- something eye catching. Photo on back cover. I'VE INCLUDED LINKS TO SOME EXAMPLES OF COVERS THAT I LIKE
Nice to have
• Designers have the flexibility to exert their creativity.I'VE INCLUDED LINKS TO SOME EXAMPLES OF COVERS THAT I LIKE
Should not have
• My picture on the cover

```html
<!DOCTYPE html>
<html lang="en">
<head>
<meta charset="utf-8">
<title>Things the Classroom Never Showed You — Book Cover</title>
<link rel="stylesheet" href="https://fonts.googleapis.com/css2?family=Anton&family=Oswald:wght@600&family=Arimo:wght@400&display=swap">
<style>
  :root {
    --page-bg: #efefef;
    --cover-bg: #ffffff;
    --ink: #111111;
    --accent: #d0111c;
    --accent-deep: #8e0a12;
    --accent-light: #f0444c;
    --rule: #222222;
  }
  * { box-sizing: border-box; margin: 0; padding: 0; }
  html, body {
    width: 1200px;
    height: 1200px;
    overflow: hidden;
    background: var(--page-bg);
  }
  .canvas {
    width: 1200px;
    height: 1200px;
    display: flex;
    align-items: center;
    justify-content: center;
  }
  .cover {
    width: 640px;
    height: 990px;
    background: var(--cover-bg);
    box-shadow: 0 10px 40px rgba(0,0,0,0.12);
    display: flex;
    flex-direction: column;
    align-items: center;
    padding: 34px 30px 0;
    text-align: center;
  }
  .title {
    display: flex;
    flex-direction: column;
    align-items: center;
    color: var(--ink);
  }
  .title-main {
    font-family: "Anton", sans-serif;
    font-size: 176px;
    line-height: 0.98;
    letter-spacing: 2px;
    text-transform: uppercase;
  }
  .title-accent {
    font-family: "Oswald", sans-serif;
    font-weight: 600;
    font-size: 47px;
    line-height: 1.1;
    color: var(--accent);
    text-transform: uppercase;
    margin: 6px 0 10px;
    letter-spacing: 0.5px;
  }
  .subtitle-block {
    width: 540px;
    border-top: 2px solid var(--rule);
    border-bottom: 2px solid var(--rule);
    margin-top: 14px;
    padding: 16px 0 18px;
  }
  .subtitle {
    font-family: "Arimo", sans-serif;
    font-size: 21px;
    line-height: 1.3;
    color: var(--ink);
    text-transform: uppercase;
  }
  .cover-art {
    width: 300px;
    height: 120px;
    margin-top: 70px;
    border-radius: 60px;
    background: radial-gradient(ellipse at 40% 35%, var(--accent-light), var(--accent) 55%, var(--accent-deep));
  }
  .author {
    font-family: "Arimo", sans-serif;
    font-size: 34px;
    color: var(--ink);
    margin-top: 60px;
    text-transform: uppercase;
    letter-spacing: 0.5px;
  }
</style>
</head>
<body>
  <main class="canvas">
    <article class="cover">
      <h1 class="title">
        <span class="title-main">Things</span>
        <span class="title-accent">The Classroom Never Showed</span>
        <span class="title-main">You</span>
      </h1>
      <div class="subtitle-block">
        <p class="subtitle">Unfiltered tips to help<br>early career professionals successfully<br>navigate the workplace</p>
      </div>
      <div class="cover-art" role="img" aria-label="Red letter dice spelling LEAD and LEARN"></div>
      <p class="author">Author Name</p>
    </article>
  </main>
</body>
</html>
```